A new art and beauty business needing a eCommerce design

I need an ecommerce design for my company that is based in Australia called 'Fern and Fable'. I make art and other products and would like the website to be an easy to use website, it must however, look modern and professional.

Could you please provide the finished product CODED with HTML etc. and ready to be used.

Colours can be chosen by the designer and are not limited in any way by our previous websites design.

I look forward to your submissions and will reward good work with our approval for payment.

If you would like further information you are welcome to ask.

Industry/Entity Type

Business

Contact Information for Business Card

Company Name: Fern and Fable

Owners Name: Darren Vollmacht

Address: 14 Copperfield Row
Tumbarra, NSW 2687
Australia

Phone: 0491 786 215

Email: contact@fern-andfable.com

Logo Text

Fern and Fable

```html
<!DOCTYPE html>
<html lang="en">
<head>
<meta charset="utf-8">
<title>Fern and Fable – Art &amp; Beauty Store</title>
<link href="https://fonts.googleapis.com/css2?family=Courgette&family=Open+Sans:wght@400;600;700&display=swap" rel="stylesheet">
<style>
:root{
  --purple:#5a2d82;
  --purple-dark:#46206a;
  --orange:#f5a31a;
  --text:#555;
  --muted:#8a8a8a;
  --line:#e2e2e2;
  --panel:#f4f4f4;
  --footer:#3a3a3a;
  --footer-deep:#2f2f2f;
  --white:#fff;
}
*{box-sizing:border-box;margin:0;padding:0}
html,body{width:781px;height:1200px;overflow:hidden}
body{font-family:"Open Sans",Arial,sans-serif;color:var(--text);background:var(--white);font-size:9px;position:relative}
.container{position:absolute;left:65px;width:651px}
.script{font-family:"Courgette",cursive}

/* header */
.site-header{top:0;height:84px;display:flex;align-items:center;justify-content:space-between}
.brand{font-family:"Courgette",cursive;color:var(--purple);font-size:26px;display:flex;align-items:center;gap:8px}
.brand-mark{width:14px;height:14px;border-radius:50%;background:var(--orange)}
.header-info{display:flex;gap:16px;align-items:center}
.perk{display:flex;align-items:center;gap:5px;font-size:7px;color:var(--muted);line-height:1.25}
.perk strong{display:block;color:#444;font-size:7.5px;font-weight:600}
.perk svg{width:18px;height:18px}
.cart{display:flex;align-items:center;gap:6px;font-size:7.5px;color:#444;line-height:1.3}
.cart-icon{width:22px;height:22px;background:var(--purple);border-radius:3px;display:flex;align-items:center;justify-content:center}
.cart b{color:var(--purple)}

/* nav */
.main-nav{top:92px;height:32px;background:var(--panel);border:1px solid var(--line);display:flex}
.main-nav a{flex:1 1 auto;display:flex;align-items:center;justify-content:center;font-size:7.5px;font-weight:600;color:#555;text-decoration:none;border-right:1px solid var(--line);letter-spacing:.3px}
.main-nav a:last-child{border-right:0}
.main-nav a.active{background:var(--orange);color:var(--white)}

/* sidebar */
.sidebar{position:absolute;left:65px;top:143px;width:182px}
.mini-product{display:flex;gap:10px;height:74px;padding:6px 0;border-bottom:1px solid var(--line)}
.mini-thumb{width:60px;height:60px;border:1px solid var(--line);padding:3px}
.mini-thumb div{width:100%;height:100%}
.mini-info{padding-top:10px;line-height:1.6}
.stars{color:var(--orange);font-size:8px;letter-spacing:1px}
.mini-info .name{font-size:7.5px;color:#666}
.mini-info .price{color:var(--purple);font-weight:700;font-size:9px}

.block-title{font-family:"Courgette",cursive;color:var(--purple);font-size:17px;padding-bottom:6px;border-bottom:2px solid var(--line);position:relative}
.block-title::after{content:"";position:absolute;left:0;bottom:-2px;width:50px;height:2px;background:var(--orange)}

.categories{position:absolute;top:268px;width:182px}
.cat-list{list-style:none;margin-top:6px}
.cat-list li{height:19.5px;display:flex;align-items:center;gap:6px;font-size:7px;color:#666;border-bottom:1px dotted #d8d8d8;letter-spacing:.2px}
.cat-list li::before{content:"";width:0;height:0;border-left:4px solid var(--orange);border-top:3px solid transparent;border-bottom:3px solid transparent}

.newsletter-side{position:absolute;top:521px;width:182px}
.newsletter-side p{font-size:7.5px;line-height:1.55;color:var(--muted);margin:10px 0 10px}
.field{height:24px;border:1px solid var(--line);font-size:7.5px;color:#aaa;display:flex;align-items:center;padding-left:8px;margin-bottom:8px}
.btn{display:inline-flex;align-items:center;justify-content:center;background:var(--orange);color:var(--white);font-weight:700;font-size:7.5px;letter-spacing:.5px;height:22px;padding:0 14px}

/* slider */
.hero{position:absolute;left:260px;top:143px;width:456px;height:222px;overflow:hidden;box-shadow:0 6px 8px -4px rgba(0,0,0,.3)}
.hero-photo{position:absolute;inset:0;background:linear-gradient(100deg,#cfcfd2 0%,#e9e9ec 30%,#b8b3c4 55%,#8f8a99 100%)}
.hero-copy{position:absolute;right:22px;top:38px;text-align:right;color:var(--white)}
.hero-copy .kicker{font-size:11px;font-weight:700;letter-spacing:1px;color:#fff}
.hero-copy h1{font-size:30px;font-weight:700;color:var(--purple);letter-spacing:1px;line-height:1.1;background:rgba(255,255,255,.75);padding:0 6px}
.hero-copy .deal{font-family:"Courgette",cursive;color:var(--orange);font-size:20px;margin-top:4px}
.hero-copy .shop-now{display:inline-block;margin-top:18px;border:1px solid var(--white);padding:5px 10px;font-size:7.5px;font-weight:700;letter-spacing:1px;background:rgba(0,0,0,.25)}
.hero-dots{position:absolute;bottom:10px;left:50%;transform:translateX(-50%);display:flex;gap:5px}
.hero-dots span{width:6px;height:6px;border-radius:50%;background:rgba(255,255,255,.6)}
.hero-dots span.on{background:var(--orange)}

/* featured */
.featured{position:absolute;left:260px;top:411px;width:456px}
.view-toggle{position:absolute;left:0;top:35px;display:flex;flex-direction:column;gap:4px}
.view-toggle span{width:10px;height:10px;background:#444;border-radius:1px}
.product-grid{display:grid;grid-template-columns:repeat(3,140px);column-gap:18px;row-gap:30px;margin-top:12px;padding-left:0}
.product-grid{margin-left:0}
.card{height:212px;text-align:center}
.card-img{height:112px;border:1px solid var(--line);padding:4px;margin-left:0}
.card-img div{width:100%;height:100%}
.card .stars{margin-top:8px;color:#ccc}
.card h3{font-size:7.5px;font-weight:700;color:#444;margin-top:4px;letter-spacing:.3px}
.card p{font-size:6.5px;color:var(--muted);line-height:1.5;margin:5px 6px 0}
.card .price{margin-top:8px;border-top:1px solid var(--line);border-bottom:1px solid var(--line);padding:5px 0;font-size:8px;color:#666}
.card .price b{color:var(--orange)}

.pager{position:absolute;right:65px;top:940px;display:flex;gap:4px}
.pager span{width:15px;height:15px;display:flex;align-items:center;justify-content:center;font-size:7.5px;color:#555;font-weight:600}
.pager span.on{background:var(--orange);color:var(--white)}

/* footer */
.footer-main{position:absolute;left:0;top:989px;width:781px;height:118px;background:var(--footer)}
.footer-cols{position:absolute;left:65px;top:12px;width:651px;display:grid;grid-template-columns:repeat(4,1fr);gap:14px}
.footer-cols h4{color:var(--white);font-size:8px;font-weight:700;letter-spacing:.5px;padding-bottom:5px;border-bottom:1px solid #555;margin-bottom:6px}
.footer-cols li{list-style:none;font-size:6.8px;color:#b8b8b8;line-height:1.9}
.footer-cols li::before{content:"› ";color:var(--orange)}
.contact li::before{content:none}
.contact li{display:flex;gap:5px;align-items:flex-start;line-height:1.7}
.contact svg{width:8px;height:8px;margin-top:3px;flex:none}

.footer-bar{position:absolute;left:0;top:1107px;width:781px;height:52px;background:var(--footer-deep)}
.footer-bar .inner{position:absolute;left:65px;width:651px;top:0;height:52px;display:flex;align-items:center;justify-content:space-between}
.news{display:flex;align-items:center;gap:6px;color:var(--white);font-size:8px;font-weight:700}
.news .input{width:90px;height:17px;background:var(--white);color:#aaa;font-weight:400;font-size:6.5px;display:flex;align-items:center;padding-left:5px}
.news .go{width:17px;height:17px;background:var(--orange)}
.follow{display:flex;align-items:center;gap:5px;color:var(--white);font-size:8px;font-weight:700}
.follow i{width:18px;height:18px;border-radius:50%;display:block}
.payments{display:flex;gap:4px}
.payments i{display:block;width:26px;height:16px;border-radius:2px;background:#e8e8e8}
.copyright{position:absolute;left:0;top:1160px;width:781px;height:40px;background:var(--purple);color:#e6dcef;font-size:7px;display:flex;align-items:center;justify-content:center;border-top:3px solid var(--purple-dark)}
</style>
</head>
<body>

<header class="container site-header">
  <div class="brand"><span class="brand-mark"></span>Fern and Fable</div>
  <div class="header-info">
    <div class="perk">
      <svg viewBox="0 0 20 20"><circle cx="10" cy="10" r="9.5" fill="#5a2d82"/><path d="M4 7h7v5H4zM11 9h3l2 2v1h-5z" fill="#fff"/><circle cx="7" cy="13.5" r="1.3" fill="#fff"/><circle cx="13.5" cy="13.5" r="1.3" fill="#fff"/></svg>
      <div><strong>Free Shipping</strong>On all orders</div>
    </div>
    <div class="perk">
      <svg viewBox="0 0 20 20"><circle cx="10" cy="10" r="9.5" fill="#5a2d82"/><rect x="6" y="9" width="8" height="6" rx="1" fill="#fff"/><path d="M7.5 9V7a2.5 2.5 0 015 0v2" stroke="#fff" fill="none" stroke-width="1.3"/></svg>
      <div><strong>Secure Payment</strong>Safe checkout</div>
    </div>
    <div class="perk">
      <svg viewBox="0 0 20 20"><circle cx="10" cy="10" r="9.5" fill="#5a2d82"/><path d="M5 5h5l5 5-5 5-5-5z" fill="#fff"/><circle cx="7.5" cy="7.5" r="1" fill="#5a2d82"/></svg>
      <div><strong>Special Offers</strong>Save up to 50%</div>
    </div>
    <div class="cart">
      <div class="cart-icon"><svg width="13" height="13" viewBox="0 0 14 14"><path d="M1 2h2l2 7h6l2-5H4" stroke="#fff" fill="none" stroke-width="1.3"/><circle cx="6" cy="12" r="1" fill="#fff"/><circle cx="10" cy="12" r="1" fill="#fff"/></svg></div>
      <div>0 ITEM(S)<br><b>$0.00</b></div>
    </div>
  </div>
</header>

<nav class="container main-nav">
  <a class="active">HOME</a><a>SERVICES</a><a>SHOP</a><a>NEWS</a><a>NEW PRODUCTS</a><a>SPECIALS</a><a>BLOG</a><a>NEWS</a><a>CONTACT US</a>
</nav>

<aside class="sidebar">
  <div class="mini-product">
    <div class="mini-thumb"><div role="img" aria-label="Colourful abstract painting" style="background:linear-gradient(135deg,#e23a8a,#f6c12a,#3a9be0)"></div></div>
    <div class="mini-info"><div class="stars">★★★★★</div><div class="name">Lorem Accessories</div><div class="price">$120.00</div></div>
  </div>
  <div class="mini-product">
    <div class="mini-thumb"><div role="img" aria-label="Bright abstract painting" style="background:linear-gradient(135deg,#f08a24,#d8327a,#f2e14a)"></div></div>
    <div class="mini-info"><div class="stars">★★★★★</div><div class="name">Lorem Accessories</div><div class="price">$120.00</div></div>
  </div>
  <div class="mini-product">
    <div class="mini-thumb"><div role="img" aria-label="Splash colour artwork" style="background:linear-gradient(135deg,#27a7d8,#e94c8b,#f7b733)"></div></div>
    <div class="mini-info"><div class="stars">★★★★★</div><div class="name">Lorem Accessories</div><div class="price">$120.00</div></div>
  </div>

  <section class="categories">
    <h2 class="block-title">Shop Categories</h2>
    <ul class="cat-list">
      <li>EVERYDAY SKINCARE</li><li>LIMITED ART PRINTS</li><li>SCENTED CANDLES</li><li>BATH AND BODY</li><li>GIFT SETS</li><li>CANVAS ARTWORK</li><li>HOME DECOR</li><li>ORIGINAL PAINTINGS</li><li>NATURAL OILS</li><li>NEW ARRIVALS</li>
    </ul>
  </section>

  <section class="newsletter-side">
    <h2 class="block-title">Stay In The Know</h2>
    <p>Sign up to our list for new art, fresh beauty products and special offers sent straight to your inbox.</p>
    <div class="field">Enter Your Name</div>
    <div class="field">Enter Your Email</div>
    <span class="btn">SUBSCRIBE</span>
  </section>
</aside>

<section class="hero">
  <div class="hero-photo" role="img" aria-label="Two purple candles in glass holders on a tabletop"></div>
  <div class="hero-copy">
    <div class="kicker">FERN AND FABLE</div>
    <h1>AUSTRALIA</h1>
    <div class="deal">50% Upto</div>
    <span class="shop-now">SHOP NOW</span>
  </div>
  <div class="hero-dots"><span class="on"></span><span></span><span></span></div>
</section>

<section class="featured">
  <h2 class="block-title">Featured Products</h2>
  <div class="product-grid">
    <article class="card"><div class="card-img"><div role="img" aria-label="Colourful abstract canvas" style="background:linear-gradient(135deg,#e43b8c,#f7c52e 50%,#2fa3e0)"></div></div><div class="stars">★★★★★</div><h3>CONTRARY TO POPULAR</h3><p>A bold hand-made canvas piece in bright tones, ready to hang.</p><div class="price"><b>$ 60.00</b> ( 40%off )</div></article>
    <article class="card"><div class="card-img"><div role="img" aria-label="Purple candles in glass holders" style="background:linear-gradient(160deg,#d9d9dd,#6a3d98 60%,#c9c6cf)"></div></div><div class="stars">★★★★★</div><h3>CONTRARY TO POPULAR</h3><p>A scented soy candle poured by hand in a clear glass holder.</p><div class="price"><b>$ 60.00</b> ( 40%off )</div></article>
    <article class="card"><div class="card-img"><div role="img" aria-label="Rainbow splash painting" style="background:linear-gradient(135deg,#f29b23,#e8447c 45%,#3bb0de)"></div></div><div class="stars">★★★★★</div><h3>CONTRARY TO POPULAR</h3><p>A rainbow splash artwork on canvas, signed by the artist.</p><div class="price"><b>$ 60.00</b> ( 40%off )</div></article>
    <article class="card"><div class="card-img"><div role="img" aria-label="Multicolour paint drip artwork" style="background:linear-gradient(135deg,#f5d33b,#e24d8d 50%,#3d8fd8)"></div></div><div class="stars">★★★★★</div><h3>CONTRARY TO POPULAR</h3><p>A drip paint canvas in warm colours for a modern living room.</p><div class="price"><b>$ 60.00</b> ( 40%off )</div></article>
    <article class="card"><div class="card-img"><div role="img" aria-label="Pale textured artwork" style="background:linear-gradient(135deg,#f3f1ee,#cfcac4 60%,#ece8e3)"></div></div><div class="stars">★★★★★</div><h3>CONTRARY TO POPULAR</h3><p>A soft neutral textured piece that suits calm, light spaces.</p><div class="price"><b>$ 60.00</b> ( 40%off )</div></article>
    <article class="card"><div class="card-img"><div role="img" aria-label="Vivid abstract canvas" style="background:linear-gradient(135deg,#f07a2a,#f2c431 40%,#e0418a)"></div></div><div class="stars">★★★★★</div><h3>CONTRARY TO POPULAR</h3><p>A vivid abstract canvas full of energy and warm summer hues.</p><div class="price"><b>$ 60.00</b> ( 40%off )</div></article>
  </div>
</section>

<div class="pager"><span>«</span><span>1</span><span>2</span><span>3</span><span>4</span><span>5</span><span>6</span><span class="on">7</span><span>8</span><span>»</span></div>

<footer>
  <div class="footer-main">
    <div class="footer-cols">
      <div><h4>MY ACCOUNT</h4><ul><li>My Orders</li><li>My Wish List</li><li>My Addresses</li><li>Personal Info</li></ul></div>
      <div><h4>INFORMATION</h4><ul><li>About Us</li><li>Delivery Info</li><li>Privacy Policy</li><li>Sitemap</li></ul></div>
      <div><h4>CUSTOMER SERVICE</h4><ul><li>Contact Us</li><li>Returns</li><li>Site Map</li><li>Gift Vouchers</li></ul></div>
      <div class="contact"><h4>CONTACT US</h4><ul>
        <li><svg viewBox="0 0 10 10"><path d="M5 0a3.5 3.5 0 00-3.5 3.5C1.5 6 5 10 5 10s3.5-4 3.5-6.5A3.5 3.5 0 005 0z" fill="#f5a31a"/></svg>14 Copperfield Row, Tumbarra, NSW 2687 Australia</li>
        <li><svg viewBox="0 0 10 10"><path d="M2 0l2 2.5-1 1.2a6 6 0 003.3 3.3L7.5 6 10 8l-1.3 1.6C4.5 9.6.4 5.5.4 1.3z" fill="#f5a31a"/></svg>Phone: 0491 786 215</li>
        <li><svg viewBox="0 0 10 10"><rect x="0" y="2" width="10" height="6.5" fill="#f5a31a"/><path d="M0 2l5 4 5-4" stroke="#3a3a3a" fill="none"/></svg>Email: contact@fern-andfable.com</li>
      </ul></div>
    </div>
  </div>
  <div class="footer-bar"><div class="inner">
    <div class="news">NEWSLETTER :<span class="input">Enter Email</span><span class="go"></span></div>
    <div class="follow">FOLLOW US :<i style="background:#3b5998"></i><i style="background:#2ba9e1"></i><i style="background:#dd4b39"></i><i style="background:#f39c12"></i><i style="background:#c4302b"></i><i style="background:#0e76a8"></i></div>
    <div class="payments"><i></i><i></i><i></i><i></i></div>
  </div></div>
  <div class="copyright">© Copy Rights 2014 Fern and Fable in Australia. All Rights Reserved.</div>
</footer>

</body>
</html>
```